Business Card & Email Signature Design || Upmarket + Luxury

Rima Vale Honey, a New Zealand Manuka Honey company needs a Business Card & Email Signature design.

Our logo's are attached in Gold & Black versions, feel free to be creative with how you use the logo and it's patterns in your design.

Style:
- Looking for an Elegant, Luxurious, Upmarket feel.
- Black/Matte Black Card, Gold Foil, UV Embossing

Information to Add:

- Logo
- Company Name: Rima Vale Honey
- Name: Martin Delrow
- Title: Creative Director
- Phone: +64 2815 90 617
- Email: martin@rimavalehoney.example.nz
- Website: www.rimavalehoney.example.nz

- Socials: ***For email Signature Only***
- Facebook: https://www.facebook.com/rimavalehoney/
- Instagram: https://www.instagram.com/rimavalehoney/

Target Market(s)

Asia/Europe Luxury, Upmarket

Contact Information for Business Card

- Logo
- Name: Martin Delrow
- Phone: +64 2815 90 617

Font styles to use
Other font styles liked:
• Champagne & Limousines (Attached)

Requirements
Must have
• Business Card & Email Signature Design.

Looking for a Sleek, Luxury, Upmarket Design.

```html
<!DOCTYPE html>
<html lang="en">
<head>
<meta charset="utf-8">
<title>Rima Vale Honey – Business Card</title>
<link rel="stylesheet" href="https://fonts.googleapis.com/css2?family=Fjalla+One&family=Montserrat:wght@400;500&display=swap">
<style>
  :root {
    --backdrop: #2a2a2c;
    --card-black: #1b1b1c;
    --card-white: #f3f3f1;
    --gold: #c9a54e;
    --royal-blue: #1f4fb8;
    --ink-grey: #4a4a4c;
  }
  * { margin: 0; padding: 0; box-sizing: border-box; }
  html, body { width: 1200px; height: 900px; overflow: hidden; }
  body {
    background: var(--backdrop);
    font-family: "Montserrat", sans-serif;
  }
  .canvas {
    position: relative;
    width: 1200px;
    height: 900px;
  }
  .card {
    position: absolute;
    left: 250px;
    width: 700px;
    height: 400px;
  }
  .card-back {
    top: 40px;
    background: var(--card-black);
    display: flex;
    align-items: center;
    justify-content: center;
    gap: 16px;
  }
  .brand-dot {
    width: 14px;
    height: 14px;
    border-radius: 50%;
    background: var(--gold);
  }
  .brand-name {
    color: var(--gold);
    font-family: "Montserrat", sans-serif;
    font-weight: 500;
    font-size: 30px;
    letter-spacing: 6px;
    text-transform: uppercase;
  }
  .card-front {
    top: 460px;
    background: var(--card-white);
  }
  .identity {
    position: absolute;
    right: 405px;
    top: 148px;
    text-align: right;
  }
  .person-name {
    font-family: "Fjalla One", sans-serif;
    color: var(--royal-blue);
    font-size: 44px;
    line-height: 1;
    letter-spacing: 1px;
    text-transform: uppercase;
  }
  .person-title {
    color: var(--ink-grey);
    font-size: 19px;
    margin-top: 8px;
  }
  .divider {
    position: absolute;
    left: 310px;
    top: 146px;
    width: 3px;
    height: 104px;
    background: var(--royal-blue);
  }
  .contact-list {
    position: absolute;
    left: 328px;
    top: 150px;
    list-style: none;
  }
  .contact-item {
    display: flex;
    align-items: center;
    gap: 8px;
    color: var(--ink-grey);
    font-size: 18px;
    line-height: 32px;
  }
  .contact-icon {
    width: 14px;
    height: 14px;
    flex: none;
  }
</style>
</head>
<body>
<main class="canvas">
  <section class="card card-back" aria-label="Card back">
    <span class="brand-dot"></span>
    <span class="brand-name">Rima Vale Honey</span>
  </section>

  <section class="card card-front" aria-label="Card front">
    <div class="identity">
      <h1 class="person-name">Martin Delrow</h1>
      <p class="person-title">Creative Director</p>
    </div>
    <div class="divider"></div>
    <ul class="contact-list">
      <li class="contact-item">
        <svg class="contact-icon" viewBox="0 0 16 16" aria-hidden="true"><path d="M4 1 L6.5 1 L7.5 5 L5.5 6.5 C6.5 8.8 7.4 9.8 9.5 10.7 L11 8.7 L15 9.7 L15 12.3 C15 14 13.5 15 12 15 C6 14.5 1.5 10 1 4 C1 2.5 2.2 1 4 1 Z" fill="var(--royal-blue)"/></svg>
        <span>+64 2815 90 617</span>
      </li>
      <li class="contact-item">
        <svg class="contact-icon" viewBox="0 0 16 16" aria-hidden="true"><rect x="1" y="3" width="14" height="10" rx="1" fill="none" stroke="var(--royal-blue)" stroke-width="1.6"/><path d="M1.5 3.8 L8 9 L14.5 3.8" fill="none" stroke="var(--royal-blue)" stroke-width="1.6"/></svg>
        <span>martin@rimavalehoney.example.nz</span>
      </li>
      <li class="contact-item">
        <svg class="contact-icon" viewBox="0 0 16 16" aria-hidden="true"><g fill="none" stroke="var(--royal-blue)" stroke-width="1.3"><circle cx="8" cy="8" r="6.6"/><ellipse cx="8" cy="8" rx="3" ry="6.6"/><path d="M1.4 8 H14.6 M2.5 4.6 H13.5 M2.5 11.4 H13.5"/></g></svg>
        <span>www.rimavalehoney.example.nz</span>
      </li>
    </ul>
  </section>
</main>
</body>
</html>
```